kf novum
My service company has specialists in Sales, Marketing and Change Management. Our target group is the 1st and 2nd management level of enterprises, who want to align their strategy at new market situations or to change their distribution, communication or product concept.
We help our clients in defined time frames or projects not only in defining new strategies and concepts but also in implementation and measurements of the results.
I'm looking for a design of business cards and A4 letter paper. The company name is "kf novum"; my name ist Konrad Fels...
So the name of my company stands for Management on time (kf novum) and kf stands for my name (initials)
Logo see enclosed.

```html
<!DOCTYPE html>
<html lang="en">
<head>
<meta charset="utf-8">
<title>kf novum – business cards</title>
<link rel="stylesheet" href="https://fonts.googleapis.com/css2?family=Montserrat:wght@300;400;600&display=swap">
<style>
  :root {
    --board: #6b6c6e;
    --navy: #23283a;
    --navy-glow: #4b4d66;
    --ink: #3a3d45;
    --ink-soft: #55585f;
    --paper: #ffffff;
    --ghost: #f2f2f4;
    --muted-mark: #5f6175;
  }
  * { box-sizing: border-box; margin: 0; padding: 0; }
  html, body { width: 1200px; height: 1008px; overflow: hidden; background: var(--board); }
  body { font-family: "Montserrat", Arial, sans-serif; color: var(--ink); }
  .board { position: relative; width: 1200px; height: 1008px; background: var(--board); }

  .card { position: absolute; width: 408px; height: 258px; background: var(--paper); overflow: hidden; }
  .card--front { left: 132px; top: 172px; }
  .card--back-a { left: 660px; top: 172px; }
  .card--dark { left: 132px; top: 576px; border-radius: 16px;
    background: radial-gradient(ellipse 60% 60% at 50% 40%, var(--navy-glow) 0%, var(--navy) 100%); }
  .card--back-b { left: 660px; top: 576px; border-radius: 16px; }

  .bar { position: absolute; background: var(--navy); }

  .ghost-disc { position: absolute; border-radius: 50%; background: var(--ghost); }

  .brand { position: absolute; font-weight: 300; letter-spacing: 0.04em; color: var(--navy); white-space: nowrap; line-height: 1; }
  .brand-dot { position: absolute; border-radius: 50%; background: var(--navy); }

  .card--front .brand-dot { left: 174px; top: 58px; width: 60px; height: 60px; }
  .card--front .brand { left: 0; width: 408px; text-align: center; top: 152px; font-size: 40px; }

  .card--dark .brand-dot { left: 174px; top: 58px; width: 60px; height: 60px; background: var(--muted-mark); }
  .card--dark .brand { left: 0; width: 408px; text-align: center; top: 152px; font-size: 40px; color: var(--muted-mark); }

  .person { position: absolute; font-size: 16px; font-weight: 400; letter-spacing: 0.08em; color: var(--ink); white-space: nowrap; }

  .contact { position: absolute; list-style: none; font-size: 11px; letter-spacing: 0.06em; color: var(--ink-soft); }
  .contact li { position: absolute; left: 0; white-space: nowrap; line-height: 14px; }
  .contact .firm { font-weight: 600; color: var(--ink); }
  .contact svg { position: absolute; left: -16px; top: 1px; width: 11px; height: 12px; fill: var(--navy); }
</style>
</head>
<body>
<main class="board">

  <!-- Front -->
  <section class="card card--front">
    <span class="brand-dot"></span>
    <span class="brand">kf novum</span>
  </section>

  <!-- Back, variant A -->
  <section class="card card--back-a">
    <span class="bar" style="left:0;top:0;width:8px;height:98px"></span>
    <span class="bar" style="left:398px;top:112px;width:10px;height:146px"></span>
    <span class="ghost-disc" style="left:-10px;top:98px;width:210px;height:210px"></span>
    <span class="brand-dot" style="left:92px;top:18px;width:36px;height:36px"></span>
    <span class="brand" style="left:41px;top:68px;font-size:19px">kf novum</span>
    <span class="person" style="left:218px;top:70px">Konrad Fels</span>
    <ul class="contact" style="left:237px;top:0">
      <li class="firm" style="top:108px"><svg viewBox="0 0 12 14"><path d="M6 0a4.5 4.5 0 0 0-4.5 4.5C1.5 8 6 14 6 14s4.5-6 4.5-9.5A4.5 4.5 0 0 0 6 0zm0 6.4a1.9 1.9 0 1 1 0-3.8 1.9 1.9 0 0 1 0 3.8z"/></svg>kf novum</li>
      <li style="top:124px">Beispielweg 7</li>
      <li style="top:140px">54321 Beispielstadt</li>
      <li style="top:164px"><svg viewBox="0 0 12 14"><path d="M2.5 1l2 .3.8 3-1.4 1c.6 1.8 1.8 3.3 3.4 4.3l1.2-1.2 2.8 1-.1 2.1C8.6 12.8 1.2 8 2.5 1z"/></svg>+49 5550 1234567</li>
      <li style="top:181px"><svg viewBox="0 0 12 14"><path d="M3 0h6a1 1 0 0 1 1 1v12a1 1 0 0 1-1 1H3a1 1 0 0 1-1-1V1a1 1 0 0 1 1-1zm.5 1.5v9h5v-9zM6 11.3a.8.8 0 1 0 0 1.6.8.8 0 0 0 0-1.6z"/></svg>+49 555 9876543</li>
      <li style="top:205px"><svg viewBox="0 0 12 14"><circle cx="6" cy="7" r="5.5"/><path d="M.5 7h11M6 1.5c-2.5 3-2.5 8 0 11M6 1.5c2.5 3 2.5 8 0 11" stroke="#fff" stroke-width=".8" fill="none"/></svg>www.kfnovum.example</li>
      <li style="top:222px"><svg viewBox="0 0 12 14"><path d="M0 3h12v8H0z"/><path d="M0 3l6 4.5L12 3" stroke="#fff" stroke-width=".9" fill="none"/></svg>info@kfnovum.example</li>
    </ul>
  </section>

  <!-- Dark front -->
  <section class="card card--dark">
    <span class="brand-dot"></span>
    <span class="brand">kf novum</span>
  </section>

  <!-- Back, variant B -->
  <section class="card card--back-b">
    <span class="bar" style="left:0;top:112px;width:8px;height:146px"></span>
    <span class="bar" style="left:398px;top:0;width:10px;height:83px"></span>
    <span class="ghost-disc" style="left:60px;top:90px;width:220px;height:220px"></span>
    <span class="brand-dot" style="left:292px;top:16px;width:36px;height:36px"></span>
    <span class="brand" style="left:249px;top:64px;font-size:19px">kf novum</span>
    <span class="person" style="left:39px;top:70px">Konrad Fels</span>
    <ul class="contact" style="left:59px;top:0">
      <li class="firm" style="top:108px"><svg viewBox="0 0 12 14"><path d="M6 0a4.5 4.5 0 0 0-4.5 4.5C1.5 8 6 14 6 14s4.5-6 4.5-9.5A4.5 4.5 0 0 0 6 0zm0 6.4a1.9 1.9 0 1 1 0-3.8 1.9 1.9 0 0 1 0 3.8z"/></svg>kf novum</li>
      <li style="top:124px">Beispielweg 7</li>
      <li style="top:140px">54321 Beispielstadt</li>
      <li style="top:164px"><svg viewBox="0 0 12 14"><path d="M2.5 1l2 .3.8 3-1.4 1c.6 1.8 1.8 3.3 3.4 4.3l1.2-1.2 2.8 1-.1 2.1C8.6 12.8 1.2 8 2.5 1z"/></svg>+49 5550 1234567</li>
      <li style="top:181px"><svg viewBox="0 0 12 14"><path d="M3 0h6a1 1 0 0 1 1 1v12a1 1 0 0 1-1 1H3a1 1 0 0 1-1-1V1a1 1 0 0 1 1-1zm.5 1.5v9h5v-9zM6 11.3a.8.8 0 1 0 0 1.6.8.8 0 0 0 0-1.6z"/></svg>+49 555 9876543</li>
      <li style="top:205px"><svg viewBox="0 0 12 14"><circle cx="6" cy="7" r="5.5"/><path d="M.5 7h11M6 1.5c-2.5 3-2.5 8 0 11M6 1.5c2.5 3 2.5 8 0 11" stroke="#fff" stroke-width=".8" fill="none"/></svg>www.kfnovum.example</li>
      <li style="top:222px"><svg viewBox="0 0 12 14"><path d="M0 3h12v8H0z"/><path d="M0 3l6 4.5L12 3" stroke="#fff" stroke-width=".9" fill="none"/></svg>info@kfnovum.example</li>
    </ul>
  </section>

</main>
</body>
</html>
```